UNABLE TO FIND SUITABLE ICT TALENT IN NEW ZEALAND? WE CAN HELP.

We need a brochure to sell our migration services to ICT (Information and Communication Technologies) recruiters in New Zealand. We are a New Zealand based migration company headed by a Licensed Immigration Adviser and we can bring in specific talents into New Zealand. We are aware ICT is in the long term skill shortage area and that recruiters and companies are struggling to find the right ICT talent. So over the past two years we have developed a high quality global ICT talent pool who are keen to work in New Zealand. And we have the expertise to and process their legal entry into New Zealand bring them in at short notice. We need a brochure that conveys a strong New Zealand connect, confidence and trust.

Target Market(s)

New Zealand ICT Recruiters and Companies who need ICT talent

Industry/Entity Type

Communication

Contact Information for Business Card

Marlow Feltis
Senior Manager - Operations
Mobile: 0213394625

Font styles to use
Serif

Requirements
Must have
• A strong ICT and New Zealand theme. Must have the following Maori proverb on the rear with the English translation. The rear side of the card which has this proverb must also have a strong Maori theme.
• Naku te rourou nau te rourou ka ora ai te iwi - With your basket and my basket the people will live
Nice to have
• The brochure/flyer is intended to be an A4 size folded in half, so that we can print and mail it to our target clients. Remember this is an A4 flyer folded in the middle. So it has got cover + back + 2 inside pages in all.

```html
<!DOCTYPE html>
<html lang="en">
<head>
<meta charset="utf-8">
<title>Tawhiri – ICT Talent Brochure</title>
<link href="https://fonts.googleapis.com/css2?family=Montserrat:wght@400;500;600;700&display=swap" rel="stylesheet">
<style>
:root{
  --stage:#3a3a3a;
  --purple:#8a1a8f;
  --purple-dark:#6e1273;
  --ink:#333333;
  --ink-soft:#4a4a4a;
  --white:#ffffff;
  --panel-dark:#1f1f21;
  --grey-light:#f4f4f4;
  --grey-mid:#cfcfcf;
}
*{margin:0;padding:0;box-sizing:border-box}
html,body{width:1200px;height:907px;overflow:hidden;background:var(--stage)}
body{position:relative;font-family:"Montserrat",Arial,sans-serif}
.brochure{position:absolute;left:95px;top:62px;width:1028px;height:733px;overflow:hidden;background:var(--white)}
.city-photo{position:absolute;left:0;top:0;width:1028px;height:503px;
  background:linear-gradient(180deg,#b9c7d6 0%,#dfe5ec 35%,#8f949b 62%,#5c5f64 80%,#7a766e 100%)}
.quote-panel{position:absolute;left:0;top:0;width:1028px;height:503px;
  background:linear-gradient(180deg,#141416 0%,var(--panel-dark) 55%,#2a2a2c 100%);
  clip-path:polygon(0 0,362px 0,497px 503px,0 503px)}
.diagonal-band{position:absolute;left:0;top:0}
.photo-circle{position:absolute;border-radius:50%;border:11px solid var(--purple);overflow:hidden;background:var(--white)}
.photo-circle .photo{width:100%;height:100%;border-radius:50%;border:4px solid var(--white)}
.circle-river{left:252px;top:43px;width:200px;height:200px}
.circle-river .photo{background:linear-gradient(135deg,#6aa83a 0%,#4d8c2a 45%,#3d8fa8 60%,#67b6c9 100%)}
.circle-coast{left:312px;top:279px;width:174px;height:174px}
.circle-coast .photo{background:linear-gradient(180deg,#cfe3ee 0%,#8fc2d3 25%,#3aa7a8 55%,#3f5a3a 100%)}
.brand-mark{position:absolute;display:flex;align-items:center;gap:8px;font-weight:700;letter-spacing:1px}
.brand-mark .dot{width:14px;height:14px;border-radius:50%}
.brand-front{left:66px;top:114px;color:var(--white);font-size:26px}
.brand-front .dot{background:var(--white)}
.brand-back{left:836px;top:603px;color:#111;font-size:28px}
.brand-back .dot{background:#111}
.proverb{position:absolute;left:42px;top:238px;width:240px;color:var(--white);font-size:17px;line-height:22px}
.proverb .mark{display:block;color:#8e8e8e;font-size:34px;font-weight:700;line-height:20px;margin-left:98px}
.proverb .mark.close{margin-top:20px}
.proverb p{margin-top:18px}
.proverb p+p{margin-top:18px}
.white-rule{position:absolute;left:0;top:500px;width:1028px;height:5px;background:var(--white)}
.purple-strip{position:absolute;left:0;top:505px;width:1028px;height:18px;background:var(--purple)}
.info-band{position:absolute;left:0;top:523px;width:1028px;height:210px;
  background:linear-gradient(90deg,#c9c9c9 0%,var(--grey-light) 30%,#fafafa 50%,#e2e2e2 51%,var(--grey-light) 75%,var(--grey-mid) 100%)}
.contact{position:absolute;left:67px;top:587px;width:400px;text-align:center;color:var(--ink-soft);font-size:15.5px;line-height:21px}
.contact .gap{margin-top:8px}
.contact .gap2{margin-top:11px}
.pitch{position:absolute;left:540px;top:559px;width:262px;text-align:right;color:var(--ink)}
.pitch .l1{font-size:18px;font-weight:500;letter-spacing:.3px}
.pitch .l2{font-size:21px;font-weight:500;margin-top:2px;letter-spacing:.2px}
.pitch .l3{font-size:23px;font-weight:700;color:var(--purple);margin-top:-2px}
.pitch .callout{margin-top:6px;border-top:2px solid var(--purple);border-bottom:2px solid var(--purple);
  text-align:center;font-size:29px;font-weight:700;color:var(--purple);padding:4px 0 3px;letter-spacing:.5px}
</style>
</head>
<body>
<div class="brochure">
  <div class="city-photo" role="img" aria-label="Photograph of a New Zealand city skyline with high-rise towers under a cloudy sky"></div>
  <div class="quote-panel" role="img" aria-label="Darkened city skyline photograph behind the proverb"></div>
  <svg class="diagonal-band" width="1028" height="503" viewBox="0 0 1028 503">
    <polygon points="360,0 382,0 517,503 495,503" fill="#8a1a8f"/>
  </svg>
  <div class="photo-circle circle-river"><div class="photo" role="img" aria-label="Aerial photograph of green mangroves beside a blue river"></div></div>
  <div class="photo-circle circle-coast"><div class="photo" role="img" aria-label="Photograph of a rocky headland and turquoise sea"></div></div>

  <div class="brand-mark brand-front"><span class="dot"></span>Tawhiri</div>

  <div class="proverb">
    <span class="mark">“</span>
    <p>Naku te rourou nau te rourou ka ora ai te iwi</p>
    <p>With your basket and my basket the people will live</p>
    <span class="mark close">”</span>
  </div>

  <div class="white-rule"></div>
  <div class="purple-strip"></div>
  <div class="info-band"></div>

  <div class="contact">
    <div>PO Box 40317, Riverlea Post Shop,</div>
    <div>Hamilton, Waikato, New Zealand</div>
    <div class="gap">Email: info@tawhiri.kiwi</div>
    <div class="gap2">www.tawhiri.kiwi</div>
  </div>

  <div class="pitch">
    <div class="l1">UNABLE TO FIND</div>
    <div class="l2">SUITABLE ICT TALENT</div>
    <div class="l3">IN NEW ZEALAND?</div>
    <div class="callout">WE CAN HELP</div>
  </div>

  <div class="brand-mark brand-back"><span class="dot"></span>Tawhiri</div>
</div>
</body>
</html>
```